Premium stylish simple clever card design for high end construction company.

I need a business card designed that is a standard size and shape (square edges) that is black in colour, with black edges. All text is to be either grey/silver or yellow/gold. On the front I want the logo (supplied as attachment g5) to be embossed or raised to give a texture. I also want the name of my company "The Quiet Ember (larger font) construction co. (smaller font)" I like the clean style (found in attachment 56419286) of the black background with silver text. But the triangle is to be gold/yellow.

On the back needs to have my contact details. In silver or gold text.

Marcus Delby - Builder
Marcus@thequietember.com.au
www.thequietember.com.au
0438201965
Lic 517904k
PO BOX 758 Wrenmoor NSW 2184

Must look simple, elegant and precise.

My work is of the utmost quality and my business card needs to project that. It needs to be simple and precise. It should scream luxury and confidence. Feel free to get creative with the font and font size. If you google "The Quiet Ember" you will see it has links to great architecture, art, nature and the fibonacci sequence so i am open to using these ideas also.

Target Market(s)

High End home owners. 30-70 year olds.

Industry/Entity Type

Residential Construction

Contact Information for Business Card

Logo and company name on front. Contact details on back.

Font styles to use
Serif
Sans Serif

Colors
ffcf3e

Requirements
Must have
• black background
Nice to have
• debossed logo (silver and gold)
• debased company name (silver)
Should not have
• It should not look like a standard construction business card with pictures of hammers or tools etc.

```html
<!DOCTYPE html>
<html lang="en">
<head>
<meta charset="utf-8">
<title>The Quiet Ember — Business Card</title>
<link rel="stylesheet" href="https://fonts.googleapis.com/css2?family=Open+Sans:wght@300;400;600;700&display=swap">
<style>
  :root {
    --stage: #e4e1db;
    --card-dark: #0c0c0c;
    --card-mid: #1d1d1d;
    --silver: #c9c9c9;
    --silver-soft: #9a9a9a;
    --gold: #ffcf3e;
    --tab: #d6d6d6;
  }
  * { margin: 0; padding: 0; box-sizing: border-box; }
  html, body {
    width: 1200px;
    height: 900px;
    overflow: hidden;
    background: var(--stage);
    font-family: "Open Sans", Arial, sans-serif;
  }
  .stage { position: relative; width: 1200px; height: 900px; }

  .card {
    position: absolute;
    width: 630px;
    height: 360px;
    border-radius: 18px;
    overflow: hidden;
    background: linear-gradient(120deg, var(--card-mid) 0%, var(--card-dark) 55%, #151515 100%);
    box-shadow: 0 18px 40px rgba(0,0,0,.35);
  }
  .card--front { left: 150px; top: 60px; }
  .card--back { left: 420px; top: 480px; }

  .wordmark {
    display: flex;
    align-items: center;
    gap: 14px;
    color: var(--silver);
    font-weight: 300;
    text-transform: uppercase;
    letter-spacing: 1px;
    white-space: nowrap;
  }
  .wordmark__dot {
    width: 14px; height: 14px;
    border-radius: 50%;
    background: var(--gold);
    flex: none;
  }
  .card--front .wordmark {
    position: absolute;
    left: 50%; top: 50%;
    transform: translate(-50%, -50%);
    font-size: 40px;
  }
  .card--back .wordmark {
    position: absolute;
    right: 40px; top: 62px;
    font-size: 29px;
  }

  .person {
    position: absolute;
    left: 92px; top: 150px;
  }
  .person__name {
    color: var(--silver);
    font-weight: 700;
    font-size: 30px;
    line-height: 1.1;
  }
  .person__role {
    color: var(--gold);
    font-size: 17px;
    margin-top: 2px;
  }
  .accent-half-disc {
    position: absolute;
    left: 0; top: 165px;
    width: 40px; height: 80px;
    border-radius: 0 40px 40px 0;
    background: var(--gold);
  }
  .base-tab {
    position: absolute;
    left: 0; bottom: 0;
    width: 300px; height: 56px;
    background: var(--tab);
    border-radius: 0 26px 0 0;
  }

  .contact {
    position: absolute;
    left: 350px; top: 150px;
    color: var(--gold);
    font-size: 15px;
    line-height: 1.35;
    white-space: nowrap;
  }
  .contact__block { margin-bottom: 12px; }
  .contact__row {
    display: flex;
    align-items: center;
    gap: 10px;
  }
  .contact__icon {
    width: 14px; height: 14px;
    flex: none;
    fill: none;
    stroke: var(--silver-soft);
    stroke-width: 1.4;
  }
</style>
</head>
<body>
<main class="stage">

  <section class="card card--front" aria-label="Card front">
    <div class="wordmark"><span class="wordmark__dot"></span>The Quiet Ember</div>
  </section>

  <section class="card card--back" aria-label="Card back">
    <div class="wordmark"><span class="wordmark__dot"></span>The Quiet Ember</div>

    <span class="accent-half-disc"></span>
    <div class="person">
      <p class="person__name">Marcus Delby</p>
      <p class="person__role">Builder</p>
    </div>

    <div class="contact">
      <div class="contact__block">
        <p>Lic 517904k</p>
        <p>PO BOX 758 Wrenmoor NSW 2184</p>
      </div>
      <p class="contact__row">
        <svg class="contact__icon" viewBox="0 0 16 16"><path d="M4 1.5 L6.5 4.5 L5 6.5 Q6.5 9.5 9.5 11 L11.5 9.5 L14.5 12 L12.5 14.5 Q5 13 1.5 3.5 Z"/></svg>
        0438201965
      </p>
      <p class="contact__row">
        <svg class="contact__icon" viewBox="0 0 16 16"><circle cx="8" cy="8" r="6.5"/><ellipse cx="8" cy="8" rx="3" ry="6.5"/><path d="M1.5 8 H14.5 M2.5 4.8 H13.5 M2.5 11.2 H13.5"/></svg>
        www.thequietember.com.au
      </p>
      <p class="contact__row">
        <svg class="contact__icon" viewBox="0 0 16 16"><rect x="1.5" y="3.5" width="13" height="9"/><path d="M1.5 3.5 L8 9 L14.5 3.5"/></svg>
        Marcus@thequietember.com.au
      </p>
    </div>

    <span class="base-tab"></span>
  </section>

</main>
</body>
</html>
```